Book for new dads needs a cover.

We need a cover for a book titled Compass for Rookie Papas: Practical Steps for Surviving the Waiting Months, Juggling Jobs and Home, and Keeping Your Head Steady Before the Little One Arrives. We would like to see a design that emphasizes healthy babies and confident dads.

```html
<!DOCTYPE html>
<html lang="en">
<head>
<meta charset="utf-8">
<title>Compass for Rookie Papas – Book Cover</title>
<link rel="stylesheet" href="https://fonts.googleapis.com/css2?family=Bebas+Neue&family=Zilla+Slab:wght@400;500&display=swap">
<style>
  :root {
    --page: #ffffff;
    --orange-core: #f8940d;
    --orange-edge: #db6c13;
    --ink: #2b2b2b;
    --paper: #ffffff;
  }
  * { margin: 0; padding: 0; box-sizing: border-box; }
  html, body {
    width: 1200px;
    height: 1200px;
    overflow: hidden;
    background: var(--page);
  }
  .cover {
    position: absolute;
    left: 200px;
    top: 0;
    width: 800px;
    height: 1200px;
    background: radial-gradient(ellipse 70% 60% at 50% 58%, var(--orange-core) 0%, #ef8410 55%, var(--orange-edge) 100%);
    overflow: hidden;
  }
  .title-main,
  .title-link,
  .title-second {
    position: absolute;
    left: 0;
    width: 100%;
    text-align: center;
    font-family: "Zilla Slab", serif;
    font-weight: 500;
    color: var(--ink);
    line-height: 1;
  }
  .title-main {
    top: 150px;
    font-size: 178px;
    letter-spacing: -2px;
  }
  .title-link {
    top: 326px;
    font-size: 62px;
    left: 20px;
  }
  .title-second {
    top: 372px;
    font-size: 132px;
    letter-spacing: -1px;
  }
  .title-hero {
    position: absolute;
    left: 58px;
    top: 518px;
    width: 690px;
    height: 294px;
  }
  .title-hero text {
    font-family: "Bebas Neue", sans-serif;
  }
  .subtitle {
    position: absolute;
    left: 70px;
    top: 902px;
    width: 660px;
    text-align: center;
    font-family: "Zilla Slab", serif;
    font-weight: 400;
    font-size: 25px;
    line-height: 38px;
    color: var(--paper);
  }
  .author {
    position: absolute;
    left: 0;
    top: 1110px;
    width: 100%;
    text-align: center;
    font-family: "Bebas Neue", sans-serif;
    font-size: 44px;
    letter-spacing: 17px;
    padding-left: 17px;
    color: var(--paper);
    line-height: 1;
  }
</style>
</head>
<body>
  <main class="cover">
    <h1>
      <span class="title-main">Compass</span>
      <span class="title-link">for</span>
      <span class="title-second">Rookie</span>
      <svg class="title-hero" viewBox="0 0 690 294" role="img" aria-label="Large white word PAPAS with silhouettes of expecting parents, a father lifting a baby and a father walking hand in hand with a toddler set inside the letters">
        <defs>
          <linearGradient id="heroFill" x1="0" y1="0" x2="0" y2="1">
            <stop offset="0" stop-color="#ffffff"/>
            <stop offset="1" stop-color="#fff6ea"/>
          </linearGradient>
        </defs>
        <text x="0" y="292" font-size="412" textLength="690" lengthAdjust="spacingAndGlyphs" fill="url(#heroFill)">PAPAS</text>
      </svg>
    </h1>
    <p class="subtitle">Practical Steps for Surviving the Waiting Months, Juggling Jobs and Home, and Keeping Your Head Steady Before the Little One Arrives</p>
    <p class="author">Author Name</p>
  </main>
</body>
</html>
```